Korvix App Graphics Design

Our application promotes location based self expression via pictures and text. The primary focus of the application is on the content posted and not on the person that posted it.

We want a very clean and fresh design that evokes positive energy. Our site is unique so our design should be as well. People will reveal thoughts on our site, so the design should convey a "revealing" feel. Our site is a place where people are comfortable to freely express themselves. Colors we have in mind are blue and green hues with earth tones for background.

Our project is to design ten screens for our Korvix application at resolution of 1136-by-640 pixels:

Feed Screen
Camera Screen
Post Screen
Check In Screen
Approval Screen
Map Screen
Flag Screen
Feed Select Screen
Export Screen
Menu Screen

In the contest phase we will require only three screens to be submitted. The screens we require to be submitted are: Feed Screen; Map Screen and Camera Screen. The designer we select as the winner of the competition will then complete the project and deliver a total of the ten screens described above in the handover phase.

We have attached a document below with detailed specs of each screen, we ask for your innovation to bring these screens to life through your design.
Updates

We want to clarify one aspect regarding the VISOR: the visor needs to be transparent so that when the picture scrolls underneath it, you can still see the picture underneath the visor.

Hi Everyone,

We have noticed that some designers need clarification regarding the visor element in the feed screen.
I have attached two examples to our brief area called:
Visor Example 1 and Visor Example 2

Please note that these are not the style we are looking for but are a good example to the concept of a Transparent Visor above the feed stream. We are looking for you guys to come up with a Visor concept that is consistent with the style of the design you are submitting.

Thanks,

Bo

Target Market(s)

People 17-40 who want to share their thought about the world around them.

Industry/Entity Type

Flag

Font styles to use
Sans Serif
Other font styles liked:
• We like “Helvetica New” or “Avenir” but are flexible

Requirements
Must have
• Visor component should look innovative.

```html
<!DOCTYPE html>
<html lang="en">
<head>
<meta charset="utf-8">
<title>Korvix — Feed</title>
<link rel="stylesheet" href="https://fonts.googleapis.com/css2?family=Nunito:ital,wght@0,700;0,800;0,900;1,800;1,900&display=swap">
<style>
:root{
  --page:#f4f4f2;
  --ink:#1a1a1a;
  --yellow:#f8e36c;
  --teal:#3fb5bd;
  --teal-soft:#8fcfb4;
  --mint:#7fc4a4;
  --red:#d8342a;
  --red-deep:#c22a22;
  --orange:#e7a53a;
  --banner-text:#c9d7e3;
  --green-bar:rgba(92,170,70,.85);
  --title:#4a4034;
  --white:#ffffff;
}
*{box-sizing:border-box;margin:0;padding:0}
html,body{width:961px;height:1200px;overflow:hidden;background:var(--page);font-family:"Nunito",sans-serif}
.screen{position:absolute;left:141px;top:0;width:678px;height:1200px;overflow:hidden;background:var(--yellow)}
.status-bar{position:absolute;left:0;top:0;width:100%;height:50px;background:var(--white);display:flex;align-items:center;justify-content:space-between;padding:0 22px}
.top-nav{position:absolute;left:0;top:50px;width:100%;height:104px;background:var(--yellow);display:flex;justify-content:space-around;align-items:center;padding:0 80px}
.header-fade{position:absolute;left:0;top:140px;width:100%;height:72px;background:linear-gradient(180deg,var(--yellow) 0%,#bfd9a0 45%,#9ccfb6 100%)}
.photo{position:absolute;left:0;top:204px;width:100%;height:660px;background:linear-gradient(90deg,#3a2a22 0%,#7a5a48 20%,#a68a76 50%,#7a5a48 80%,#3a2a22 100%)}
.visor{position:absolute;left:0;top:210px;width:100%;height:118px;background:rgba(231,165,58,.72);display:flex;align-items:center;justify-content:center}
.visor-text{font-weight:900;font-style:italic;font-size:50px;color:var(--banner-text);letter-spacing:.5px}
.flag-tab{position:absolute;left:0;top:364px;width:64px;height:80px;background:var(--red);border-radius:0 40px 40px 0;display:flex;align-items:center;justify-content:center}
.share-rail{position:absolute;right:0;top:360px;width:70px;height:364px;background:var(--red);border-radius:30px 0 0 30px;display:flex;flex-direction:column;justify-content:space-around;align-items:center;padding:14px 0}
.share-item{font-weight:800;font-size:15px;color:var(--yellow)}
.stats-bar{position:absolute;left:0;top:784px;width:100%;height:56px;background:var(--green-bar);display:flex;align-items:center;justify-content:space-between;padding:0 14px;color:var(--white);font-weight:900;font-size:30px}
.stat{display:flex;align-items:center;gap:6px}
.stat small{font-size:18px;font-weight:800}
.actions{position:absolute;left:0;top:864px;width:100%;height:144px;display:flex}
.action{flex:1;display:flex;align-items:center;justify-content:center}
.action-save{background:linear-gradient(135deg,var(--teal-soft),var(--teal) 60%,#86c9c0)}
.action-boost{background:linear-gradient(135deg,var(--red-deep),var(--red) 50%,var(--orange))}
.place{position:absolute;left:0;top:1008px;width:100%;height:100px;background:var(--yellow);text-align:center;color:var(--title);padding-top:16px}
.place-name{font-size:34px;line-height:1.15;font-weight:900;font-style:italic}
.place-address{font-size:27px;line-height:1.2;font-weight:900;font-style:italic}
.bottom-nav{position:absolute;left:0;top:1108px;width:100%;height:92px;background:var(--mint);display:flex;align-items:center;justify-content:space-between;padding:0 60px 0 70px}
.page-count{font-weight:800;font-size:56px;color:var(--white)}
</style>
</head>
<body>
<main class="screen">
  <div class="status-bar">
    <svg width="70" height="30" viewBox="0 0 70 30" aria-hidden="true">
      <rect x="0" y="20" width="5" height="8" fill="var(--ink)"/><rect x="8" y="15" width="5" height="13" fill="var(--ink)"/><rect x="16" y="10" width="5" height="18" fill="var(--ink)"/><rect x="24" y="4" width="5" height="24" fill="var(--ink)"/>
      <path d="M38 12 a20 20 0 0 1 28 0" stroke="var(--ink)" stroke-width="4" fill="none"/><path d="M43 18 a12 12 0 0 1 18 0" stroke="var(--ink)" stroke-width="4" fill="none"/><circle cx="52" cy="24" r="3" fill="var(--ink)"/>
    </svg>
    <svg width="44" height="24" viewBox="0 0 44 24" aria-hidden="true"><rect x="2" y="3" width="40" height="18" rx="6" fill="none" stroke="var(--ink)" stroke-width="4"/><rect x="9" y="9" width="26" height="6" fill="var(--ink)"/></svg>
  </div>

  <nav class="top-nav">
    <svg width="56" height="66" viewBox="0 0 56 66" aria-label="Posts"><rect x="4" y="4" width="48" height="58" rx="6" fill="none" stroke="var(--teal)" stroke-width="6"/><path d="M16 20h24M16 32h24M16 44h24" stroke="var(--teal)" stroke-width="5"/></svg>
    <svg width="50" height="68" viewBox="0 0 50 68" aria-label="Nearby"><path d="M25 64C12 46 5 34 5 24a20 20 0 0 1 40 0c0 10-7 22-20 40z" fill="none" stroke="var(--teal)" stroke-width="6" stroke-linejoin="round"/><circle cx="25" cy="24" r="7" fill="var(--teal)"/></svg>
    <svg width="64" height="64" viewBox="0 0 64 64" aria-label="Search"><circle cx="26" cy="26" r="18" fill="none" stroke="var(--teal)" stroke-width="7"/><path d="M40 40l18 18" stroke="var(--teal)" stroke-width="10" stroke-linecap="round"/></svg>
  </nav>
  <div class="header-fade"></div>

  <div class="photo" role="img" aria-label="Upward view of an ornate terracotta building facade with carved piers"></div>

  <div class="visor"><p class="visor-text">I love this building!</p></div>

  <div class="flag-tab">
    <svg width="36" height="36" viewBox="0 0 36 36" aria-label="Flag post"><path d="M6 34V4" stroke="var(--yellow)" stroke-width="4"/><path d="M8 5c8-4 12 4 24 0v16c-12 4-16-4-24 0z" fill="var(--yellow)"/></svg>
  </div>

  <aside class="share-rail">
    <span class="share-item">Rovo</span>
    <span class="share-item">Chir</span>
    <span class="share-item">Pinl</span>
    <span class="share-item">Lumo</span>
    <span class="share-item">Gplx</span>
  </aside>

  <div class="stats-bar">
    <span class="stat"><svg width="26" height="26" viewBox="0 0 26 26" aria-hidden="true"><circle cx="13" cy="13" r="11" fill="var(--white)"/><path d="M7 8c3 1 4 4 2 6s1 5 3 7M16 4c-1 3 2 5 5 5" stroke="var(--green-bar)" stroke-width="2.5" fill="none"/></svg>3.5 <small>MI</small></span>
    <span class="stat"><svg width="10" height="24" viewBox="0 0 10 24" aria-hidden="true"><rect x="1" y="2" width="8" height="20" fill="var(--white)"/></svg>99</span>
    <span class="stat"><svg width="28" height="28" viewBox="0 0 28 28" aria-hidden="true"><circle cx="14" cy="14" r="11" fill="none" stroke="var(--white)" stroke-width="3"/><path d="M14 7v7l5 3" stroke="var(--white)" stroke-width="3" fill="none"/></svg>3 <small>HRS</small></span>
  </div>

  <section class="actions">
    <div class="action action-save"><svg width="42" height="104" viewBox="0 0 42 104" aria-label="Save"><path d="M0 0h42v104L21 82 0 104z" fill="var(--white)"/></svg></div>
    <div class="action action-boost"><svg width="52" height="110" viewBox="0 0 52 110" aria-label="Boost"><path d="M34 0L6 58h18L14 110 48 44H30z" fill="var(--white)"/></svg></div>
  </section>

  <section class="place">
    <h1 class="place-name">Halvorsen Tower</h1>
    <p class="place-address">27 Linden Ave, Marrow Falls, NY 10000</p>
  </section>

  <nav class="bottom-nav">
    <svg width="84" height="66" viewBox="0 0 84 66" aria-label="Camera"><path d="M4 14h20l6-10h24l6 10h20v48H4z" fill="var(--white)"/><circle cx="42" cy="38" r="15" fill="var(--mint)"/><circle cx="42" cy="38" r="9" fill="var(--white)"/></svg>
    <svg width="84" height="76" viewBox="0 0 84 76" aria-label="Next"><path d="M4 24h38V5l36 33-36 33V52H4z" fill="none" stroke="var(--white)" stroke-width="6" stroke-linejoin="round"/></svg>
    <span class="page-count">01</span>
  </nav>
</main>
</body>
</html>
```